One page flyer for nonprofit focused IT company

I need a one page flyer (one side of a single 8.5x11 page) with text and graphics. The company logo is already done, and it must appear on the flyer along with other icons and graphics. The final design will be printed on heavy weight glossy paper as a handout and also distributed as a PDF.

The text is provided in an attachment, if it needs to be shortened let me know.

Industry/Entity Type

Information Technology

Requirements
Must have
• some flare (colors, icons or images)
Should not have
• While we work for nonprofits, my company is a FOR PROFIT company.

```html
<!DOCTYPE html>
<html lang="en">
<head>
<meta charset="utf-8">
<title>Lanthorn Civic Technology – Nonprofit IT Services Flyer</title>
<link href="https://fonts.googleapis.com/css2?family=Montserrat:wght@500;700;800&family=Roboto:wght@400;700&display=swap" rel="stylesheet">
<style>
  :root{
    --brand-red:#8c1a2c;
    --title-red:#9a1b2f;
    --navy:#1d2a3f;
    --charcoal:#3b3b3d;
    --ink:#2a2a2a;
    --paper:#ffffff;
    --backdrop:#e6e6e6;
  }
  *{box-sizing:border-box;margin:0;padding:0}
  html,body{width:1200px;height:2667px;overflow:hidden;background:var(--backdrop)}
  .flyer{position:absolute;left:60px;top:1300px;width:1080px;height:1260px;background:linear-gradient(135deg,#fff 55%,#f3f3f3);box-shadow:0 6px 24px rgba(0,0,0,.18);overflow:hidden}
  .masthead{position:absolute;left:0;top:0;width:100%;height:128px}
  .masthead-rule{position:absolute;top:114px;height:5px;background:var(--brand-red)}
  .masthead-rule.left{left:0;width:405px}
  .masthead-rule.right{right:0;width:385px}
  .masthead-rule::after{content:"";position:absolute;left:0;right:0;top:7px;height:2px;background:var(--navy)}
  .brand{position:absolute;left:0;right:0;top:76px;text-align:center;font-family:Montserrat,sans-serif;font-weight:700;font-size:24px;color:var(--brand-red);letter-spacing:.5px;white-space:nowrap}
  .hero{position:absolute;left:0;top:128px;width:100%;height:305px;background:var(--navy)}
  .hero-title{position:absolute;left:25px;top:0;width:395px;height:100%;background:var(--brand-red);color:#fff;font-family:Montserrat,sans-serif;display:flex;flex-direction:column;justify-content:center;align-items:center;text-align:center;white-space:nowrap}
  .hero-title .big{font-weight:800;font-size:60px;line-height:1}
  .hero-title .mid{font-weight:500;font-size:42px;line-height:1.2;margin:6px 0 4px}
  .hero-photo{position:absolute;left:420px;top:0;right:0;height:100%;background:radial-gradient(circle at 72% 55%,#2e4666 0%,#1d2a3f 55%,#141d2c 100%)}
  .services{position:absolute;left:62px;top:458px;width:950px;display:flex;gap:50px}
  .col{width:450px}
  .service{margin-bottom:18px}
  .service-head{display:flex;align-items:center;gap:12px;margin-bottom:6px}
  .service-icon{flex:0 0 42px;height:42px}
  .service-title{font-family:Montserrat,sans-serif;font-weight:700;font-size:17px;line-height:1.05;color:var(--title-red)}
  .service p{font-family:Roboto,sans-serif;font-size:16px;line-height:1.2;color:var(--ink);text-align:justify}
  .service strong{font-weight:700}
  .footer{position:absolute;left:0;bottom:0;width:100%;height:66px}
  .footer-shape{position:absolute;inset:0;width:100%;height:100%}
  .contact{position:absolute;top:0;height:66px;display:flex;align-items:center;gap:10px;font-family:Montserrat,sans-serif;font-weight:700;font-size:16px;color:#fff;white-space:nowrap}
  .contact-icon{flex:0 0 22px;width:22px;height:22px}
</style>
</head>
<body>
<main class="flyer">
  <header class="masthead">
    <div class="brand">LANTHORN CIVIC TECHNOLOGY</div>
    <div class="masthead-rule left"></div>
    <div class="masthead-rule right"></div>
  </header>

  <section class="hero">
    <div class="hero-title">
      <span class="big">50 YEARS</span>
      <span class="mid">OF NONPROFIT</span>
      <span class="big">IT SERVICES</span>
    </div>
    <div class="hero-photo" role="img" aria-label="Photo of a businessman in a navy suit cupping his hands around a glowing cloud icon"></div>
  </section>

  <section class="services">
    <div class="col">
      <article class="service">
        <div class="service-head">
          <svg class="service-icon" viewBox="0 0 46 46"><circle cx="23" cy="23" r="20" fill="none" stroke="var(--navy)" stroke-width="2"/><path d="M23 3a20 20 0 0 1 0 40" fill="none" stroke="var(--brand-red)" stroke-width="3"/><circle cx="23" cy="23" r="7" fill="none" stroke="var(--ink)" stroke-width="2"/><circle cx="23" cy="23" r="2" fill="var(--ink)"/></svg>
          <h2 class="service-title">An Efficient and Elegant Approach to IT Solution Implementations</h2>
        </div>
        <p>Lanthorn Civic Technology has been supporting the Information Systems needs of nonprofits for over 50 years. We continually strive to bring the latest technologies and best practices to nonprofits to drive down the cost of IT while implementing systems that drive revenue. Our Agile approach to IT management means that we deliver working systems to every one of our clients every two weeks.</p>
      </article>
      <article class="service">
        <div class="service-head">
          <svg class="service-icon" viewBox="0 0 46 46"><circle cx="23" cy="23" r="20" fill="none" stroke="var(--navy)" stroke-width="2"/><path d="M23 3a20 20 0 0 1 0 40" fill="none" stroke="var(--brand-red)" stroke-width="3"/><rect x="14" y="15" width="18" height="16" fill="none" stroke="var(--ink)" stroke-width="2"/><path d="M18 20h10M18 25h10" stroke="var(--ink)" stroke-width="2"/></svg>
          <h2 class="service-title">Successes 90% Reduction in Software Development Costs</h2>
        </div>
        <p>The Harlow Regional Auto Retailers Council needed to update their core product offering; they engaged their in-house IT department who estimated the project would take 3 years at a cost of $3,000,000. HRARC decided to work with Lanthorn Civic Technology instead, and the product was released to production in only 9 months at <strong>one tenth of the cost</strong>, only $300,000</p>
      </article>
      <article class="service">
        <div class="service-head">
          <svg class="service-icon" viewBox="0 0 46 46"><circle cx="23" cy="23" r="20" fill="none" stroke="var(--navy)" stroke-width="2"/><path d="M23 3a20 20 0 0 1 0 40" fill="none" stroke="var(--brand-red)" stroke-width="3"/><rect x="13" y="16" width="20" height="14" rx="2" fill="none" stroke="var(--ink)" stroke-width="2"/><circle cx="19" cy="23" r="2.5" fill="var(--ink)"/><path d="M24 21h6M24 25h6" stroke="var(--ink)" stroke-width="2"/></svg>
          <h2 class="service-title">10x Increase in Membership</h2>
        </div>
        <p>Greenway Paths Trust needed to move to online membership registration and contracted with Lanthorn Civic Technology to build a significant online presence and engage potential members. Through compelling online tools and mobile applications Greenway Paths Trust has <strong>increased membership 10 fold.</strong></p>
      </article>
      <article class="service">
        <div class="service-head">
          <svg class="service-icon" viewBox="0 0 46 46"><circle cx="23" cy="23" r="20" fill="none" stroke="var(--navy)" stroke-width="2"/><path d="M23 3a20 20 0 0 1 0 40" fill="none" stroke="var(--brand-red)" stroke-width="3"/><ellipse cx="23" cy="15" rx="8" ry="3" fill="none" stroke="var(--ink)" stroke-width="2"/><path d="M15 15v15c0 2 16 2 16 0V15M15 22c0 2 16 2 16 0" fill="none" stroke="var(--ink)" stroke-width="2"/></svg>
          <h2 class="service-title">Member Donor Database</h2>
        </div>
        <p>Lanthorn Civic Technology's GiveLedger Member / Donor CRM system is fully customized for each client meeting the unique needs of your organization.</p>
      </article>
    </div>

    <div class="col">
      <article class="service">
        <div class="service-head">
          <svg class="service-icon" viewBox="0 0 46 46"><circle cx="23" cy="23" r="20" fill="none" stroke="var(--navy)" stroke-width="2"/><path d="M23 3a20 20 0 0 1 0 40" fill="none" stroke="var(--brand-red)" stroke-width="3"/><path d="M15 14h16l-3 18H18z" fill="none" stroke="var(--ink)" stroke-width="2"/><path d="M23 18v10M20 21h6" stroke="var(--ink)" stroke-width="2"/></svg>
          <h2 class="service-title">20% Reduction in Overhead</h2>
        </div>
        <p>The Women's Civic League had antiquated systems and processes in place to manage over 500 chapters across the nation. Working with LCT they implemented online tools to allow communication and management between the local chapters and national headquarters. This eliminated much of the overhead of chapter management, <strong>reducing HR costs by 20%.</strong></p>
      </article>
      <article class="service">
        <div class="service-head">
          <svg class="service-icon" viewBox="0 0 46 46"><circle cx="23" cy="23" r="20" fill="none" stroke="var(--navy)" stroke-width="2"/><path d="M23 3a20 20 0 0 1 0 40" fill="none" stroke="var(--brand-red)" stroke-width="3"/><rect x="17" y="12" width="12" height="22" rx="2" fill="none" stroke="var(--ink)" stroke-width="2"/><circle cx="23" cy="30" r="1.5" fill="var(--ink)"/></svg>
          <h2 class="service-title">Mobile Applications</h2>
        </div>
        <p>Lanthorn Civic Technology implements mobile applications for every major phone platform to provide direct communications with members and donors enabling real-time, two way interaction.</p>
      </article>
      <article class="service">
        <div class="service-head">
          <svg class="service-icon" viewBox="0 0 46 46"><circle cx="23" cy="23" r="20" fill="none" stroke="var(--navy)" stroke-width="2"/><path d="M23 3a20 20 0 0 1 0 40" fill="none" stroke="var(--brand-red)" stroke-width="3"/><circle cx="16" cy="17" r="3" fill="none" stroke="var(--ink)" stroke-width="2"/><circle cx="30" cy="17" r="3" fill="none" stroke="var(--ink)" stroke-width="2"/><circle cx="23" cy="30" r="3" fill="none" stroke="var(--ink)" stroke-width="2"/><path d="M18 19l4 8M28 19l-4 8M19 17h8" stroke="var(--ink)" stroke-width="2"/></svg>
          <h2 class="service-title">Systems Integration</h2>
        </div>
        <p>Every nonprofit's IT applications are scattered and disconnected. Lanthorn Civic Technology has decades of experience integrating these applications into a single cohesive system.</p>
      </article>
      <article class="service">
        <div class="service-head">
          <svg class="service-icon" viewBox="0 0 46 46"><circle cx="23" cy="23" r="20" fill="none" stroke="var(--navy)" stroke-width="2"/><path d="M23 3a20 20 0 0 1 0 40" fill="none" stroke="var(--brand-red)" stroke-width="3"/><rect x="14" y="13" width="18" height="20" fill="none" stroke="var(--ink)" stroke-width="2"/><path d="M18 29v-5M23 29v-9M28 29v-7" stroke="var(--ink)" stroke-width="2"/></svg>
          <h2 class="service-title">Business Intelligence and Reporting</h2>
        </div>
        <p>Lanthorn Civic Technology can wrestle all of an organization's data into simple executive dashboards and reports.</p>
      </article>
      <article class="service">
        <div class="service-head">
          <svg class="service-icon" viewBox="0 0 46 46"><circle cx="23" cy="23" r="20" fill="none" stroke="var(--navy)" stroke-width="2"/><path d="M23 3a20 20 0 0 1 0 40" fill="none" stroke="var(--brand-red)" stroke-width="3"/><path d="M16 29a5 5 0 0 1 1-10 7 7 0 0 1 13 1 4.5 4.5 0 0 1 0 9z" fill="none" stroke="var(--ink)" stroke-width="2"/></svg>
          <h2 class="service-title">Cloud Migration</h2>
        </div>
        <p>Reduce IT costs by migrating to the latest cloud solutions.</p>
      </article>
    </div>
  </section>

  <footer class="footer">
    <svg class="footer-shape" viewBox="0 0 1080 66" preserveAspectRatio="none" aria-hidden="true">
      <polygon points="0,0 630,0 612,66 0,66" fill="var(--brand-red)"/>
      <polygon points="650,0 1080,0 1080,66 630,66" fill="var(--charcoal)"/>
    </svg>
    <div class="contact" style="left:72px">
      <svg class="contact-icon" viewBox="0 0 22 22"><circle cx="11" cy="11" r="10" fill="none" stroke="#fff" stroke-width="1.5"/><path d="M7.5 6.5l2 0 1 2.5-1.3 1a6 6 0 0 0 3 3l1-1.3 2.5 1 0 2c-4.5.5-8.7-3.7-8.2-8.2z" fill="#fff"/></svg>
      555-014-2738
    </div>
    <div class="contact" style="left:312px">
      <svg class="contact-icon" viewBox="0 0 22 22"><circle cx="11" cy="11" r="10" fill="none" stroke="#fff" stroke-width="1.5"/><rect x="6" y="7.5" width="10" height="7" fill="none" stroke="#fff" stroke-width="1.4"/><path d="M6 7.5l5 4 5-4" fill="none" stroke="#fff" stroke-width="1.4"/></svg>
      info@lanthorntech.com
    </div>
    <div class="contact" style="left:745px">
      <svg class="contact-icon" viewBox="0 0 22 22"><circle cx="11" cy="11" r="10" fill="none" stroke="#fff" stroke-width="1.5"/><circle cx="11" cy="11" r="6" fill="none" stroke="#fff" stroke-width="1.2"/><ellipse cx="11" cy="11" rx="2.6" ry="6" fill="none" stroke="#fff" stroke-width="1.2"/><path d="M5 11h12" stroke="#fff" stroke-width="1.2"/></svg>
      www.lanthorntech.com
    </div>
  </footer>
</main>
</body>
</html>
```